Harbinger Noble Alloys Works Business Cards

We are wanting to have a new business card designed for our company as we go to a convention. We want to balance business/Modern with elegance and beauty. Our company sells highend jewelry pieces. We want to utilize the colors of Black and Gold and have gold foiled fonts to be physically printed on the business cards.
We also would like to have space to write notes on the back side of the business card. When we meet people at jewelry conventions we would like to write notes if possible.
Here are websites and designs that we like the look and feel of these companies and you can use these as design ideas.
https://www.lorvanne.com
https://www.bellquist.com/en-us/home
Here is our company website link
www.harbingernaw.com
I also up loaded two versions of our logo.
- Update 4.26.22
I have uploaded photos of a business card we like. this card has raised embossed letters that you can feel. the raise letters are like a plastic but we don't need to use that...I uploaded to show you that we like the experience of the client feeling the characters of the logo. we also would like to have the material as a satin or some material very soft.
- Maybe we can get designs with beautiful gold foiling and raised characters and logos. we like simplicity...not busy but an elegant design. We need to write notes and would like a section where we can write notes. but we want an elegant style and the client has an experience with the feel of the card when they touch the card.
Colors
- Main colors Black & Gold
- white or light colors for small notes section.
Specialty ideals and things we would like to see based on your design styles.
- raised fonts
- raised logos
- gold foiling
- satin/soft finish on the card material.
we are wanting to design a business card that looks elegant and clean. When the client is handed the business card we want them to physically experience the business card as well by touching the raised logos or fonts and the base material is soft satin. I hope this helps with further designs.
thank you all
We uploaded a new contact layout that we have designed in our office. we would like to see how this would look on your designs.
thank you
I just finished uploading the Contact Layout. the colors are just examples. please use this layout as an idea and use colors based on the feed back we have given each of you personally.
Contact Information for Business Card
we need an area to write notes, we would like to have our logos or the diamond of our logo or the business card to have embossed sections to the business card so when the customer touches the card they can feel the logo. we would also like sections of our business card to have gold foiling. we would also like to use a satin soft paper with our card. when the client touches the card its super soft and high quality
Requirements
Must have
- we would like to have our logos or the diamond of our logo or the business card to have embossed sections to the business card so when the customer touches the card they can feel the logo. we would also like sections of our business card to have gold foiling. we would also like to use a satin soft paper with our card. when the client touches the card its super soft and high quality
Nice to have
- we would like to have our logos or the diamond of our logo or the business card to have embossed sections to the business card so when the customer touches the card they can feel the logo. we would also like sections of our business card to have gold foiling.

```html
<!DOCTYPE html>
<html lang="en">
<head>
<meta charset="utf-8">
<title>Harbinger Noble Alloys Works — Business Cards</title>
<link rel="stylesheet" href="https://fonts.googleapis.com/css2?family=Cinzel:wght@500&family=Tinos:wght@400;700&display=swap">
<style>
  :root {
    --stage: #2a2a2a;
    --card: #070707;
    --white: #f4f4f2;
    --gold: #c9a45c;
    --gold-deep: #a8843e;
    --note: #ffffff;
  }
  * { box-sizing: border-box; margin: 0; padding: 0; }
  html, body { width: 1200px; height: 900px; overflow: hidden; }
  body {
    background: var(--stage);
    font-family: "Tinos", "Times New Roman", serif;
    color: var(--white);
    position: relative;
  }
  .card {
    position: absolute;
    left: 250px;
    width: 700px;
    height: 400px;
    background: var(--card);
    border-radius: 26px;
    box-shadow: 0 18px 40px rgba(0,0,0,.45);
  }
  .card--front { top: 30px; }
  .card--back { top: 470px; }

  .brand { position: absolute; text-align: center; }
  .brand__name {
    font-family: "Cinzel", "Times New Roman", serif;
    font-weight: 500;
    font-size: 30px;
    letter-spacing: 1px;
    color: var(--white);
    line-height: 1.1;
  }
  .brand__tagline {
    font-family: "Cinzel", "Times New Roman", serif;
    font-size: 17px;
    letter-spacing: 1.5px;
    color: var(--white);
    margin-top: 4px;
  }
  .card--front .brand { left: 150px; top: 62px; width: 460px; }
  .card--back .brand { left: 70px; top: 70px; width: 460px; }

  .notes__label {
    position: absolute;
    right: 30px;
    top: 140px;
    font-size: 22px;
    color: var(--gold);
    letter-spacing: .5px;
  }
  .notes__frame {
    position: absolute;
    left: 175px;
    top: 175px;
    width: 500px;
    height: 190px;
    border: 1.5px solid var(--gold);
    padding: 12px;
  }
  .notes__area {
    width: 100%;
    height: 100%;
    background: linear-gradient(100deg, #e9e9e7 0%, var(--note) 60%, #f3f3f3 100%);
  }

  .person {
    position: absolute;
    right: 330px;
    top: 195px;
    text-align: right;
  }
  .person__role { font-size: 18px; color: var(--white); }
  .person__name {
    font-size: 20px;
    font-weight: 700;
    color: var(--gold);
    letter-spacing: 1px;
    margin-top: 4px;
  }
  .divider {
    position: absolute;
    left: 388px;
    top: 170px;
    width: 1px;
    height: 170px;
    background: var(--gold-deep);
  }
  .contact {
    position: absolute;
    left: 412px;
    top: 160px;
    list-style: none;
    font-size: 16px;
    line-height: 1.35;
  }
  .contact__item { display: flex; align-items: flex-start; gap: 10px; margin-bottom: 18px; }
  .contact__item--tight { margin-bottom: 4px; }
  .contact__icon { width: 16px; height: 16px; flex: none; margin-top: 2px; fill: var(--gold); }
</style>
</head>
<body>

  <section class="card card--front" aria-label="Card front with notes area">
    <div class="brand">
      <div class="brand__name">Harbinger Noble Alloys</div>
      <div class="brand__tagline">— Coins, Jewelry &amp; Diamonds —</div>
    </div>
    <div class="notes__label">Customer Review Here</div>
    <div class="notes__frame"><div class="notes__area"></div></div>
  </section>

  <section class="card card--back" aria-label="Card back with contact details">
    <div class="brand">
      <div class="brand__name">Harbinger Noble Alloys</div>
      <div class="brand__tagline">— Coins, Jewelry &amp; Diamonds —</div>
    </div>
    <div class="person">
      <div class="person__role">Director</div>
      <div class="person__name">EVAN MARLOW</div>
    </div>
    <div class="divider"></div>
    <ul class="contact">
      <li class="contact__item" style="margin-bottom:28px">
        <svg class="contact__icon" viewBox="0 0 16 16"><path d="M3 2l3 0 1 3-2 1.5c.8 1.8 2.2 3.2 4 4L10.5 9l3 1v3c0 .6-.4 1-1 1C6.6 14 2 9.4 2 3.5 2 2.4 2.4 2 3 2z"/></svg>
        <span>(555) 214-7390</span>
      </li>
      <li class="contact__item contact__item--tight">
        <svg class="contact__icon" viewBox="0 0 16 16"><path d="M1 3h14v10H1z M2 4.2v.6l6 4 6-4v-.6z" fill-rule="evenodd"/></svg>
        <span>info@harbingernaw.com</span>
      </li>
      <li class="contact__item">
        <svg class="contact__icon" viewBox="0 0 16 16"><circle cx="8" cy="8" r="7"/><path d="M1 8h14M8 1c-3 3-3 11 0 14M8 1c3 3 3 11 0 14" stroke="#070707" stroke-width="1" fill="none"/></svg>
        <span>www.harbingernaw.com</span>
      </li>
      <li class="contact__item">
        <svg class="contact__icon" viewBox="0 0 16 16"><path d="M8 1a5 5 0 0 1 5 5c0 4-5 9-5 9S3 10 3 6a5 5 0 0 1 5-5zm0 3a2 2 0 1 0 0 4 2 2 0 0 0 0-4z" fill-rule="evenodd"/></svg>
        <span>742 Alder Crest Ave NE<br>Salem, Oregon USA 97305</span>
      </li>
    </ul>
  </section>

</body>
</html>
```